Business Card Design Project (Beer industry)

I am seeking a redesign of my business card. I am looking for something that will really stand out in both texture and feel. Something more on the modern side then traditional. Nothing die cut shaped like a beer mug please.

The card is used mostly for other industry professionals, as well as bar and restaurant owners. My title is Strategy & Acquisitions. If you would like to somehow incorporate that theme, that may work.

My business is craft and imported beer. Nothing fizzy and yellow, so my products are more on the upscale side.
Updates

I was able to update my logo in .ai and .tif format. I hope that helps. 

Thank you all for your creative ideas. I have uploaded my current business card in pdf format, as well as our logo in .eps file format. We are excited about the submissions so far and want to thank you all again.

PS Please do not include fax number in future submissions, as we are looking for something more creative and a fax says 1999 and not 2015, which is the message we are going for, without being futuristic. 

Thank you all once again for all of your submissions. If we would consider a two sided card, we would like the opposite side not to be the same as the front. The styles we have seen so far, it appears the front and back are too similar. Again, a two sided card is not required. Thank you and we look forward to pushing the boundaries of your creativity. Cheers

Target Market(s)

My card would mostly go to bar and restaurant operators as well as other beer industry professionals

Industry/Entity Type

Restaurant

Requirements
Nice to have
• Two sided would be considered, although not required
Should not have
• Anything die cut shaped like a beer mug.

```html
<!DOCTYPE html>
<html lang="en">
<head>
<meta charset="utf-8">
<title>Kestrel Brew – Business Card</title>
<link rel="stylesheet" href="https://fonts.googleapis.com/css2?family=PT+Sans:ital,wght@0,400;0,700;1,400&display=swap">
<style>
  :root {
    --paper: #ffffff;
    --panel-blue: #2a5592;
    --panel-deep: #1f4680;
    --sky-blue: #3d6fb0;
    --frame-gold: #f6d157;
    --star-gold: #f2c744;
    --beer-amber: #e9a531;
    --ink: #111111;
    --dots: #9a9a9a;
    --address-white: #f2f4f8;
  }
  html, body {
    margin: 0;
    padding: 0;
    width: 741px;
    height: 1200px;
    overflow: hidden;
    background: var(--paper);
  }
  .card {
    position: relative;
    width: 741px;
    height: 1200px;
    background: var(--paper);
    font-family: "PT Sans", Arial, sans-serif;
  }
  .brand-panel {
    position: absolute;
    left: 0;
    top: 0;
  }
  .skyline-art {
    position: absolute;
    left: 150px;
    top: 62px;
    width: 441px;
    height: 300px;
    border-radius: 18px 18px 0 0;
    background:
      radial-gradient(ellipse 90px 110px at 50% 72%, var(--beer-amber) 0%, rgba(233,165,49,0.55) 45%, rgba(233,165,49,0) 100%),
      linear-gradient(180deg, var(--panel-blue) 0%, var(--sky-blue) 55%, var(--panel-deep) 100%);
  }
  .brand-name {
    position: absolute;
    left: 80px;
    width: 587px;
    top: 382px;
    margin: 0;
    text-align: center;
    font-size: 76px;
    line-height: 90px;
    font-weight: 700;
    letter-spacing: 1px;
    color: var(--frame-gold);
  }
  .address {
    position: absolute;
    left: 80px;
    width: 587px;
    top: 598px;
    margin: 0;
    text-align: center;
    font-style: italic;
    font-size: 21px;
    line-height: 28px;
    color: var(--address-white);
  }
  .holder {
    position: absolute;
    left: 0;
    width: 741px;
    top: 778px;
    text-align: center;
    color: var(--ink);
  }
  .holder-name {
    margin: 0;
    font-size: 36px;
    font-weight: 700;
    line-height: 40px;
  }
  .holder-title {
    margin: 0;
    font-size: 31px;
    font-style: italic;
    line-height: 36px;
  }
  .dotted-rule {
    width: 385px;
    height: 0;
    margin: 10px auto 12px;
    border-top: 5px dotted var(--ink);
  }
  .contact {
    margin: 0;
    font-size: 28px;
    line-height: 35px;
  }
  .footer-rule {
    position: absolute;
    left: 0;
    top: 1176px;
  }
</style>
</head>
<body>
<main class="card">
  <svg class="brand-panel" width="741" height="760" viewBox="0 0 741 760" aria-hidden="true">
    <path d="M80,0 H667 V628 A105,105 0 0 0 562,733 H185 A105,105 0 0 0 80,628 Z" fill="var(--panel-blue)"/>
    <path d="M92,0 V616.6 A117,117 0 0 1 196.4,721 H550.6 A117,117 0 0 1 655,616.6 V0" fill="none" stroke="var(--frame-gold)" stroke-width="4"/>
    <g class="divider-stars" fill="var(--star-gold)">
      <line x1="302" y1="582" x2="348" y2="582" stroke="var(--star-gold)" stroke-width="1.5"/>
      <line x1="394" y1="582" x2="440" y2="582" stroke="var(--star-gold)" stroke-width="1.5"/>
      <polygon points="349,576 351,580.5 356,581 352,584 353.5,589 349,586 344.5,589 346,584 342,581 347,580.5"/>
      <polygon points="371,570 373,574.5 378,575 374,578 375.5,583 371,580 366.5,583 368,578 364,575 369,574.5"/>
      <polygon points="393,576 395,580.5 400,581 396,584 397.5,589 393,586 388.5,589 390,584 386,581 391,580.5"/>
    </g>
  </svg>

  <div class="skyline-art" role="img" aria-label="Illustration of a city skyline with a harbour statue, stars and a glass of golden beer"></div>

  <p class="brand-name">KESTREL BREW</p>

  <p class="address">42 Mercer Lane<br>Brooklyn, NY 11200<br>Phone: (718) 555-0142</p>

  <section class="holder">
    <p class="holder-name">Dan Reval</p>
    <p class="holder-title">Strategy &amp; Acquisitions</p>
    <div class="dotted-rule"></div>
    <p class="contact">Cell: (917) 555-0198<br>dreval@kestrelmail.com<br>www.kestrelbrew.com</p>
  </section>

  <svg class="footer-rule" width="741" height="24" viewBox="0 0 741 24" aria-hidden="true">
    <line x1="10" y1="12" x2="352" y2="12" stroke="var(--dots)" stroke-width="4" stroke-linecap="round" stroke-dasharray="0 8"/>
    <line x1="390" y1="12" x2="732" y2="12" stroke="var(--dots)" stroke-width="4" stroke-linecap="round" stroke-dasharray="0 8"/>
    <polygon points="370,0 373.5,8 382,8.5 375.5,14 377.5,22.5 370,18 362.5,22.5 364.5,14 358,8.5 366.5,8" fill="#333333"/>
  </svg>
</main>
</body>
</html>
```